Our Family Values Printed on Canvas for our Home

My family has decided on the following values:

Be Grateful
Act Kindly
Stay Honest
Smile Often
Do Your Best
Live Adventurously
Never Stop Learning
Help Others
Love Always

We desire to print a sign (on 16x20 or 20x16 canvas) for various rooms in our house to remind us of the family we want to be. Each value has equal value, and we want the sign to reflect that (for example, we don't want one value to appear larger than another). We are not particular about colors or images however here are some hints about us that may help:
- My wife's favorite color is dark teal
- We live in the Pacific Northwest
- We love nature
- My wife and I have two sons and a dog

We look forward to your design!

--Tobias

Target Market(s)

Our family and friends

Industry/Entity Type

Non-Profit

Font styles to use
Decorative

Requirements
Must have
• - Printable on 16x20 or 20x60 canvas
• - Equal emphasis on each value
• - Easy to read

```html
<!DOCTYPE html>
<html lang="en">
<head>
<meta charset="utf-8">
<title>Family Values Canvas</title>
<link rel="stylesheet" href="https://fonts.googleapis.com/css2?family=Playfair+Display:wght@500&display=swap">
<style>
  :root {
    --wall: #f1efec;
    --teal-top: #0b7c5a;
    --teal-mid: #0a4a3a;
    --teal-deep: #051816;
    --ink: #fbfaf6;
  }
  html, body {
    margin: 0;
    padding: 0;
    width: 1200px;
    height: 801px;
    overflow: hidden;
    background: var(--wall);
  }
  .values-sign {
    position: absolute;
    left: 125px;
    top: 20px;
    width: 950px;
    height: 760px;
    display: block;
  }
  .value-line {
    font-family: "Playfair Display", "Bodoni Moda", serif;
    font-weight: 500;
    font-size: 64px;
    fill: var(--ink);
  }
</style>
</head>
<body>
<svg class="values-sign" viewBox="0 0 950 760" xmlns="http://www.w3.org/2000/svg">
  <defs>
    <linearGradient id="forest-fade" x1="0" y1="0" x2="0" y2="1">
      <stop offset="0" stop-color="var(--teal-top)"/>
      <stop offset="0.45" stop-color="var(--teal-mid)"/>
      <stop offset="1" stop-color="var(--teal-deep)"/>
    </linearGradient>
  </defs>
  <rect class="mountain-backdrop" width="950" height="760" fill="url(#forest-fade)"
        role="img" aria-label="Misty layered mountain ridges fading into deep green"/>
  <g class="value-list">
    <text class="value-line" x="285" y="130">Be Grateful</text>
    <text class="value-line" x="351" y="199">Act Kindly</text>
    <text class="value-line" x="223" y="268">Stay Honest</text>
    <text class="value-line" x="347" y="338">Smile Often</text>
    <text class="value-line" x="213" y="407">Do Your Best</text>
    <text class="value-line" x="174" y="476">Live Adventurously</text>
    <text class="value-line" x="149" y="546">Never Stop Learning</text>
    <text class="value-line" x="316" y="615">Help Others</text>
    <text class="value-line" x="277" y="684">Love Always</text>
  </g>
</svg>
</body>
</html>
```